Two Day Training Event includes a Dinner/Bowling Party at Larkspur in Troy, MI

I would like a postcard to attract Insurance Agents to an QWT meeting calling it a summit or something like that. Just something to mail to insurance agents telling them about our upcoming event with over 20 carriers. An opportunity to certify face to face with MAPD carriers and see what 2020 has to offer. Prior to OEP OPen Enrollment and AEP Annual Election period we have a number of meetings. Carriers want to come especially if we can get a number of agents. We are going to go to Larkspur a fun bowling alley for dinner, drinks and bowling to network and talk about the upcoming year.

Target Market(s)

Existing and new insurance agents

Industry/Entity Type

Insurance Broker

Contact Information for Business Card

Looking for a new card design I sent my LOGO and can upload my existing card.

Font styles to use
Serif

Colors

Designer to choose colors to be used in the design.

Requirements
Must have
• Dates Sept 16 and 17th
• location Harrowgate Conference Hall in Troy MI
• times
Nice to have
• It would be nice to see a fun design.

```html
<!DOCTYPE html>
<html lang="en">
<head>
<meta charset="utf-8">
<title>QWT Two Days Training Event – Postcard</title>
<link rel="stylesheet" href="https://fonts.googleapis.com/css2?family=Cinzel:wght@400&family=Libre+Baskerville:wght@400;700&family=Lato:wght@400;700;900&display=swap">
<style>
  :root {
    --bg: #e6e6e6;
    --navy: #1c1a5a;
    --navy-deep: #141b33;
    --red: #dc1e3c;
    --red-dark: #b51f25;
    --red-fold: #8e1519;
    --cream: #f3efe2;
    --white: #ffffff;
    --ink: #2a2a2a;
    --line: #555555;
  }
  * { box-sizing: border-box; margin: 0; padding: 0; }
  html, body { width: 902px; height: 1200px; overflow: hidden; background: var(--bg); }
  .canvas { position: relative; width: 902px; height: 1200px; }

  .postcard {
    position: absolute; width: 706px; height: 480px; background: var(--white);
    box-shadow: 0 3px 10px rgba(0,0,0,.25); overflow: hidden;
  }
  .postcard--front { left: 67px; top: 90px; }
  .postcard--back { left: 170px; top: 672px; }

  /* FRONT */
  .header-band {
    position: absolute; left: 0; top: 0; width: 706px; height: 202px; background: var(--navy);
    text-align: center; color: var(--white);
  }
  .header-band__title {
    font-family: "Cinzel", serif; font-weight: 400; font-size: 56px; letter-spacing: 6px;
    position: absolute; top: 32px; width: 100%;
  }
  .header-band__rule {
    position: absolute; left: 62px; top: 98px; width: 582px; height: 26px;
  }
  .header-band__invite {
    font-family: "Libre Baskerville", serif; font-size: 29px; color: var(--red);
    position: absolute; top: 116px; width: 100%;
  }
  .header-band__event {
    font-family: "Libre Baskerville", serif; font-size: 21px; letter-spacing: .5px;
    position: absolute; top: 160px; width: 100%;
  }
  .details-panel {
    position: absolute; left: 30px; top: 202px; width: 648px; height: 248px;
    background: var(--cream); border: 3px double var(--navy); border-top: none; border-width: 0 4px 4px 4px;
  }
  .date-ribbon { position: absolute; left: 278px; top: 202px; width: 428px; height: 102px; }
  .date-ribbon__text {
    position: absolute; left: 362px; top: 202px; width: 344px; height: 83px; color: var(--white); text-align: center;
  }
  .date-ribbon__date { font-family: "Libre Baskerville", serif; font-weight: 700; font-size: 26px; margin-top: 8px; }
  .date-ribbon__date sup { font-size: 15px; }
  .date-ribbon__time {
    font-family: "Libre Baskerville", serif; font-weight: 700; font-size: 14px; margin-top: 6px;
    display: flex; align-items: center; justify-content: center; gap: 8px;
  }
  .venue-pin { position: absolute; left: 515px; top: 273px; width: 26px; height: 26px; }
  .venue {
    position: absolute; left: 400px; top: 308px; width: 258px; text-align: center;
    font-family: "Libre Baskerville", serif; font-weight: 700; font-size: 13.5px; line-height: 20px; color: var(--ink);
  }
  .brand-name {
    position: absolute; font-family: "Libre Baskerville", serif; font-weight: 700; color: var(--navy);
  }
  .brand-name--front { left: 62px; top: 278px; font-size: 46px; }
  .contact-bar {
    position: absolute; background: var(--red-dark); color: var(--white);
    font-family: "Libre Baskerville", serif; font-size: 15px; display: flex; align-items: center; justify-content: center;
  }
  .contact-bar--front { left: 130px; top: 382px; width: 438px; height: 38px; }
  .contact-bar__label { font-size: 13px; margin-right: 22px; }
  .party-icon {
    position: absolute; width: 56px; height: 62px; border-radius: 6px; background: #d9d3c1;
  }
  .party-icon--glasses { left: 60px; top: 368px; }
  .party-icon--bowling { left: 583px; top: 368px; width: 70px; }

  /* BACK */
  .promo-photo {
    position: absolute; left: 0; top: 0; width: 386px; height: 360px;
    background: radial-gradient(circle at 70% 65%, #3b4f72 0%, #1d2a44 45%, var(--navy-deep) 100%);
  }
  .promo-ribbon { position: absolute; left: 20px; top: 22px; width: 366px; height: 68px; }
  .promo-ribbon__text {
    position: absolute; left: 86px; top: 22px; width: 300px; height: 62px; text-align: center;
    font-family: "Libre Baskerville", serif;
  }
  .promo-ribbon__small { font-size: 11.5px; color: #3a2a2a; margin-top: 9px; }
  .promo-ribbon__big { font-size: 18px; font-weight: 700; color: var(--white); margin-top: 4px; }
  .promo-copy {
    position: absolute; left: 22px; top: 124px; width: 200px; text-align: center;
    font-family: "Lato", sans-serif; color: var(--white);
  }
  .promo-copy__lead { font-size: 24px; font-weight: 700; }
  .promo-copy__body { font-size: 16.5px; font-weight: 700; line-height: 22px; margin-top: 2px; }
  .promo-copy__offer { font-size: 22px; font-weight: 900; color: var(--red); line-height: 26px; margin-top: 18px; }
  .brand-strip { position: absolute; left: 0; top: 360px; width: 386px; height: 62px; background: var(--cream); }
  .brand-name--back { left: 0; width: 386px; text-align: center; top: 10px; font-size: 34px; }
  .contact-bar--back { left: 0; top: 422px; width: 386px; height: 58px; font-size: 13.5px; }
  .contact-bar--back .contact-bar__label { font-size: 13px; margin-right: 10px; }
  .stamp-box { position: absolute; left: 591px; top: 40px; width: 80px; height: 75px; border: 1px solid #888; }
  .address-line { position: absolute; left: 424px; width: 246px; border-top: 1px solid var(--line); }
</style>
</head>
<body>
<div class="canvas">

  <section class="postcard postcard--front" aria-label="Postcard front">
    <div class="details-panel"></div>
    <header class="header-band">
      <h1 class="header-band__title">Save the Date</h1>
      <svg class="header-band__rule" viewBox="0 0 582 26" aria-hidden="true">
        <line x1="10" y1="6" x2="572" y2="6" stroke="#fff" stroke-width="1.5"/>
        <line x1="70" y1="14" x2="150" y2="14" stroke="#fff" stroke-width="1.5"/>
        <line x1="432" y1="14" x2="512" y2="14" stroke="#fff" stroke-width="1.5"/>
      </svg>
      <p class="header-band__invite">YOU ARE INVITED</p>
      <p class="header-band__event">to QWT Two Days Training Event</p>
    </header>

    <svg class="date-ribbon" viewBox="0 0 428 102" aria-hidden="true">
      <polygon points="0,34 84,0 84,83 30,102 0,62" fill="var(--red-fold)"/>
      <polygon points="84,0 428,0 428,83 84,83" fill="var(--red)"/>
      <polygon points="0,34 84,0 84,83 30,102" fill="var(--red-dark)"/>
    </svg>
    <div class="date-ribbon__text">
      <p class="date-ribbon__date">SEPT 16<sup>TH</sup> AND 17<sup>TH</sup></p>
      <p class="date-ribbon__time">
        <svg width="16" height="16" viewBox="0 0 16 16" aria-hidden="true"><circle cx="8" cy="9" r="6" fill="none" stroke="#fff" stroke-width="1.5"/><line x1="8" y1="9" x2="8" y2="5.5" stroke="#fff" stroke-width="1.5"/><line x1="6" y1="1.5" x2="10" y2="1.5" stroke="#fff" stroke-width="1.5"/></svg>
        00:00 AM
      </p>
    </div>
    <svg class="venue-pin" viewBox="0 0 26 26" aria-hidden="true">
      <circle cx="13" cy="13" r="13" fill="#fff"/>
      <path d="M13 6a4.5 4.5 0 0 0-4.5 4.5C8.5 14 13 19.5 13 19.5s4.5-5.5 4.5-9A4.5 4.5 0 0 0 13 6z" fill="var(--ink)"/>
      <circle cx="13" cy="10.5" r="1.6" fill="#fff"/>
    </svg>
    <p class="venue">Harrowgate Conference Hall<br>in Troy MI</p>

    <p class="brand-name brand-name--front">QWT</p>

    <div class="party-icon party-icon--glasses" role="img" aria-label="Champagne glasses icon"></div>
    <div class="contact-bar contact-bar--front">
      <span class="contact-bar__label">CONTACT US :</span>
      <span>(555) 214-7730 / (800) 555-0192</span>
    </div>
    <div class="party-icon party-icon--bowling" role="img" aria-label="Bowling pins and ball icon"></div>
  </section>

  <section class="postcard postcard--back" aria-label="Postcard back">
    <div class="promo-photo" role="img" aria-label="Photo of a businessman's open hands holding a glowing insurance network diagram"></div>
    <svg class="promo-ribbon" viewBox="0 0 366 68" aria-hidden="true">
      <polygon points="0,28 66,0 66,62 24,68" fill="var(--red-dark)"/>
      <polygon points="66,0 366,0 366,62 66,62" fill="var(--red)"/>
    </svg>
    <div class="promo-ribbon__text">
      <p class="promo-ribbon__small">WELCOME TO OUR UPCOMING EVENT</p>
      <p class="promo-ribbon__big">WITH OVER 20 CARRIERS</p>
    </div>
    <div class="promo-copy">
      <p class="promo-copy__lead">An opportunity</p>
      <p class="promo-copy__body">to certify face to face<br>with MAPD carriers<br>and see</p>
      <p class="promo-copy__offer">WHAT 2020 HAS<br>TO OFFER.</p>
    </div>
    <div class="brand-strip">
      <p class="brand-name brand-name--back">QWT</p>
    </div>
    <div class="contact-bar contact-bar--back">
      <span class="contact-bar__label">CONTACT US :</span>
      <span>(555) 214-7730 / (800) 555-0192</span>
    </div>
    <div class="stamp-box"></div>
    <div class="address-line" style="top:244px"></div>
    <div class="address-line" style="top:286px"></div>
    <div class="address-line" style="top:334px"></div>
  </section>

</div>
</body>
</html>
```